Design of a chocolate packaging

In hand-lettering-style: "Thank you for your work - you are an important part of our team!" (in big letters - almost 2/3 of the whole place) "This chocolate is a lot, so you enter into a raffle and have a great chance of a Velora Kip and many more great winnings ... all the information is below www.tvk-sonnenkreis.de! Good luck !!! " (in small letters underneath) The place is: 7,3cm * 15,3cm (crosswise)

Script

```html
<!DOCTYPE html>
<html lang="de">
<head>
<meta charset="utf-8">
<title>Danke für Deine Arbeit – Schokoladenbanderole</title>
<link rel="stylesheet" href="https://fonts.googleapis.com/css2?family=Great+Vibes&family=Noto+Serif:ital,wght@0,700;1,700&family=Oswald:wght@300&display=swap">
<style>
  :root {
    --page-bg: #ffffff;
    --choc-deep: #1e0c06;
    --choc-mid: #3a180b;
    --choc-warm: #5a2c14;
    --bronze: #a8713f;
    --bronze-light: #c89564;
    --bronze-dark: #6e4020;
  }
  * { margin: 0; padding: 0; box-sizing: border-box; }
  html, body {
    width: 1200px; height: 900px; overflow: hidden;
    background: var(--page-bg);
  }
  .wrapper {
    position: absolute; left: 410px; top: 37px;
    width: 380px; height: 826px;
    overflow: hidden;
    background: var(--choc-deep);
  }
  .drape {
    position: absolute; left: 0; right: 0; top: 0; height: 560px;
    background:
      radial-gradient(ellipse 80% 55% at 45% 40%, rgba(110,55,25,0.55), transparent 75%),
      linear-gradient(180deg, var(--choc-mid) 0%, var(--choc-warm) 45%, var(--choc-mid) 85%, #2a1108 100%);
  }
  .ornament-band {
    position: absolute; left: 0; right: 0; top: 515px; height: 95px;
    background: linear-gradient(180deg, rgba(42,17,8,0) 0%, rgba(168,113,63,0.45) 40%, rgba(122,74,38,0.35) 60%, #2a1108 100%);
  }
  .lower-field {
    position: absolute; left: 0; right: 0; top: 610px; bottom: 0;
    background: radial-gradient(ellipse 65% 50% at 50% 35%, #55290f 0%, #2a1108 70%, var(--choc-deep) 100%);
  }
  .headline {
    position: absolute; left: 0; top: 0; width: 380px;
    font-family: "Great Vibes", cursive;
    color: var(--bronze);
    text-shadow: 1px 1px 0 var(--bronze-dark), -1px -1px 0 rgba(230,180,130,0.3);
  }
  .headline span { position: absolute; white-space: nowrap; line-height: 1; }
  .headline .l1 { left: 22px; top: 32px; font-size: 98px; transform: rotate(7deg); }
  .headline .l2 { left: 26px; top: 170px; font-size: 96px; transform: rotate(-14deg); }
  .headline .l3 { left: 112px; top: 250px; font-size: 100px; transform: rotate(-12deg); }
  .team-line {
    position: absolute; left: 40px; top: 340px; width: 320px;
    font-family: "Noto Serif", serif; font-weight: 700;
    font-size: 31px; line-height: 1.1; text-align: center;
    color: var(--bronze);
    text-shadow: 1px 1px 0 var(--bronze-dark);
    transform: rotate(-8deg);
  }
  .raffle-note {
    position: absolute; left: 44px; top: 624px; width: 292px;
    font-family: "Noto Serif", serif; font-weight: 700; font-style: italic;
    font-size: 12.5px; line-height: 1.42; text-align: center;
    color: var(--bronze-light);
  }
  .site-url {
    position: absolute; left: 0; right: 0; top: 772px;
    font-family: "Oswald", sans-serif; font-weight: 300;
    font-size: 18px; letter-spacing: 2px; text-align: center;
    color: var(--bronze);
  }
</style>
</head>
<body>
  <div class="wrapper">
    <div class="drape" role="img" aria-label="Weich fallender Satinstoff in dunklem Schokoladenbraun"></div>
    <div class="ornament-band" role="img" aria-label="Geschwungenes bronzefarbenes Schmuckband"></div>
    <div class="lower-field"></div>
    <div class="headline">
      <span class="l1">Danke</span>
      <span class="l2">für Deine</span>
      <span class="l3">Arbeit</span>
    </div>
    <p class="team-line">Du bist ein<br>wichtiger<br>Teil unseres<br>Teams!</p>
    <p class="raffle-note">Diese Schokolade ist ein Los. Du nimmst damit an einer Verlosung Teil und hast großartige Chancen auf einen Velora Kip und viele weitere tolle Gewinne...alle Infos gibt es unter www.tvk-sonnenkreis.de! Viel Glück!!!</p>
    <p class="site-url">www.tvk-sonnenkreis.de</p>
  </div>
</body>
</html>
```